Law Firm Business Card

This is a business card for a law firm that serves US military and veterans.

The card must have ONLY the following (we want an uncluttered look):

- Company logo (PNG, GIF, JPEG copies uploaded)
- A tagline reading: "a law firm for service members and veterans"
- My name and title: "Martin Kovel" and "Attorney"
- My email: "mart.kovel@bramblecourtlegal.com"
- My number: "855-MOKE-TIB (665-3842)"

We are looking for a clean, simple layout with only the above information, likely printed on a bright white cotton stock. The font of our logo is DIN 1451, and the font used on our website is Helvetica Neue. The color of our logo is #336699, and we probably want the tagline in that color also, and my contact information in a dark grey. Please review our website at www.bramblecourtlegal.com to ensure your card design complements our website style.

Thanks and we look forward to seeing your submissions.

A few notes:

- Two-sided submissions are ok
- Please don't add graphics (scales of justice, judges hammer, etc)

```html
<!DOCTYPE html>
<html lang="en">
<head>
<meta charset="utf-8">
<title>Bramble Court Legal – Business Card</title>
<link rel="stylesheet" href="https://fonts.googleapis.com/css2?family=Roboto+Condensed:wght@300;400&display=swap">
<style>
  :root {
    --brand-blue: #336699;
    --text-grey: #555a60;
    --card-white: #ffffff;
    --backdrop: #e6e7e9;
  }
  * { margin: 0; padding: 0; box-sizing: border-box; }
  html, body {
    width: 1200px;
    height: 900px;
    overflow: hidden;
    background: var(--backdrop);
  }
  .stage {
    width: 1200px;
    height: 900px;
    display: flex;
    align-items: center;
    justify-content: center;
  }
  .business-card {
    width: 840px;
    height: 480px;
    background: var(--card-white);
    box-shadow: 0 6px 24px rgba(0,0,0,0.12);
    display: flex;
    flex-direction: column;
    align-items: center;
    justify-content: center;
    text-align: center;
    font-family: "Roboto Condensed", "Helvetica Neue", Arial, sans-serif;
  }
  .firm-name {
    color: var(--brand-blue);
    font-size: 52px;
    font-weight: 400;
    line-height: 1.1;
  }
  .tagline {
    margin-top: 22px;
    font-size: 23px;
    font-weight: 400;
    color: var(--text-grey);
    line-height: 1.1;
  }
  .star-row {
    display: block;
    margin-top: 6px;
  }
  .attorney-name {
    margin-top: 6px;
    font-size: 36px;
    font-weight: 400;
    color: var(--brand-blue);
    line-height: 1.05;
  }
  .attorney-title {
    font-size: 18px;
    font-weight: 400;
    color: var(--text-grey);
    line-height: 1.1;
  }
  .contact {
    margin-top: 26px;
    font-size: 22px;
    color: var(--text-grey);
    line-height: 1.15;
    font-style: normal;
  }
</style>
</head>
<body>
  <main class="stage">
    <section class="business-card">
      <h1 class="firm-name">Bramble Court Legal</h1>
      <p class="tagline">a law firm for service members and veterans</p>
      <svg class="star-row" width="378" height="16" viewBox="0 0 378 16" aria-hidden="true">
        <defs>
          <polygon id="star" points="8,0.5 9.9,5.8 15.5,5.9 11,9.3 12.7,14.8 8,11.5 3.3,14.8 5,9.3 0.5,5.9 6.1,5.8" fill="var(--brand-blue)"/>
        </defs>
        <use href="#star" x="0"/><use href="#star" x="21"/><use href="#star" x="42"/>
        <use href="#star" x="63"/><use href="#star" x="84"/><use href="#star" x="105"/>
        <use href="#star" x="126"/><use href="#star" x="147"/><use href="#star" x="168"/>
        <use href="#star" x="189"/><use href="#star" x="210"/><use href="#star" x="231"/>
        <use href="#star" x="252"/><use href="#star" x="273"/><use href="#star" x="294"/>
        <use href="#star" x="315"/><use href="#star" x="336"/><use href="#star" x="357"/>
      </svg>
      <h2 class="attorney-name">Martin Kovel</h2>
      <p class="attorney-title">Attorney</p>
      <address class="contact">
        <span class="contact-email">mart.kovel@bramblecourtlegal.com</span><br>
        <span class="contact-phone">855-MOKE-TIB (665-3842)</span>
      </address>
    </section>
  </main>
</body>
</html>
```